Ridgeway Sparks Business cards

We require somebody to design business cards for our new business.

Target Market(s)

Mining, haulage and civil.

Industry/Entity Type

Auto electrician in mining industry

Contact Information for Business Card

ABN, business email address, mobile number.

Colors
00AB8E
00BBA5
67D7C9
C6EFE9
E9F9F6

Requirements
Must have
• Services I offer: Breakdowns, Field Service, A/C Systems, Machine rewires, mine site vehicle fit outs

```html
<!DOCTYPE html>
<html lang="en">
<head>
<meta charset="utf-8">
<title>Ridgeway Sparks Business Cards</title>
<link href="https://fonts.googleapis.com/css2?family=Poppins:wght@400;600&display=swap" rel="stylesheet">
<style>
  :root {
    --backdrop: #161616;
    --card: #232323;
    --teal: #55c3b7;
    --teal-light: #8fdcd3;
    --text: #f1f1f1;
    --silver-dark: #7d7d7d;
    --silver-light: #e2e2e2;
    --ghost: #2d2d2d;
  }
  * { margin: 0; padding: 0; box-sizing: border-box; }
  html, body {
    width: 1200px; height: 1059px; overflow: hidden;
    background: var(--backdrop);
    font-family: "Poppins", sans-serif;
    color: var(--text);
  }
  .canvas { position: relative; width: 1200px; height: 1059px; }
  .card {
    position: absolute;
    background: var(--card);
    border-radius: 18px;
    overflow: hidden;
    box-shadow: 0 10px 24px rgba(0,0,0,0.55);
  }
  .card--front { left: 257px; top: 89px; width: 687px; height: 390px; }
  .card--back { left: 254px; top: 547px; width: 693px; height: 394px; }

  .brand {
    position: absolute; left: 478px; top: 178px; width: 180px;
    display: flex; align-items: center; gap: 8px;
    font-weight: 600; font-size: 21px; line-height: 1.1;
    color: var(--teal); text-transform: uppercase;
  }
  .brand__square { width: 14px; height: 14px; background: var(--teal); flex: none; }

  .person { position: absolute; left: 39px; top: 174px; }
  .person__name {
    font-weight: 600; font-size: 28px; letter-spacing: 0.5px;
    color: var(--teal); line-height: 1.1;
  }
  .person__role { font-size: 18px; line-height: 1.3; }

  .divider {
    position: absolute; left: 38px; top: 248px; width: 611px; height: 1.5px;
    background: var(--teal);
  }
  .contacts { position: absolute; left: 39px; top: 267px; list-style: none; }
  .contacts li {
    display: flex; align-items: center; gap: 8px;
    font-size: 18px; height: 29.5px;
  }
  .contacts svg { width: 14px; height: 14px; fill: var(--teal); }

  .footer-band {
    position: absolute; left: 0; bottom: 0; width: 100%; height: 14px;
  }

  .brand-ghost {
    position: absolute; left: 0; top: 90px; width: 100%;
    text-align: center; font-weight: 600; font-size: 40px;
    color: var(--ghost); text-transform: uppercase; letter-spacing: 1px;
  }
  .services-heading {
    position: absolute; left: 46px; top: 270px; width: 600px;
    display: flex; align-items: center; gap: 14px;
    font-weight: 600; font-size: 19px; color: var(--teal);
    white-space: nowrap;
  }
  .services-heading::before, .services-heading::after {
    content: ""; flex: 1; height: 1.5px; background: var(--teal);
  }
  .services {
    position: absolute; left: 30px; top: 303px; width: 633px;
    display: flex; flex-wrap: wrap; justify-content: center;
    column-gap: 12px; row-gap: 4px; list-style: none;
    font-size: 18px;
  }
  .services li::before { content: "•"; color: var(--teal); margin-right: 5px; font-size: 14px; }
</style>
</head>
<body>
<div class="canvas">

  <section class="card card--front">
    <div class="brand"><span class="brand__square"></span><span>Ridgeway Sparks</span></div>

    <div class="person">
      <h1 class="person__name">MARCUS HALE</h1>
      <p class="person__role">Founder/CEO</p>
    </div>

    <div class="divider"></div>

    <ul class="contacts">
      <li>ABN: 71320946</li>
      <li>
        <svg viewBox="0 0 24 24" aria-hidden="true"><path d="M6.6 10.8a15.1 15.1 0 0 0 6.6 6.6l2.2-2.2c.3-.3.7-.4 1-.2 1.1.4 2.3.6 3.6.6.6 0 1 .4 1 1V20c0 .6-.4 1-1 1C10.6 21 3 13.4 3 4c0-.6.4-1 1-1h3.5c.6 0 1 .4 1 1 0 1.3.2 2.5.6 3.6.1.3 0 .7-.2 1z"/></svg>
        123.480.5617
      </li>
      <li>
        <svg viewBox="0 0 24 24" aria-hidden="true"><path d="M2 5h20v14H2z" fill="none"/><path d="M2 5h20v14H2V5zm2 2v.4l8 5.2 8-5.2V7H4zm0 2.8V17h16V9.8l-8 5.2-8-5.2z"/></svg>
        info@ridgewaysparks.com
      </li>
    </ul>

    <svg class="footer-band" viewBox="0 0 687 14" preserveAspectRatio="none" aria-hidden="true">
      <defs>
        <linearGradient id="tealBand" x1="0" x2="1">
          <stop offset="0" stop-color="#4dbbb0"/>
          <stop offset="0.5" stop-color="#8fdcd3"/>
          <stop offset="1" stop-color="#4dbbb0"/>
        </linearGradient>
        <linearGradient id="silverBand" x1="0" x2="1">
          <stop offset="0" stop-color="#6f6f6f"/>
          <stop offset="0.3" stop-color="#e2e2e2"/>
          <stop offset="0.55" stop-color="#8a8a8a"/>
          <stop offset="0.8" stop-color="#dcdcdc"/>
          <stop offset="1" stop-color="#7a7a7a"/>
        </linearGradient>
      </defs>
      <polygon points="0,0 346,0 332,14 0,14" fill="url(#tealBand)"/>
      <polygon points="354,0 687,0 687,14 340,14" fill="url(#silverBand)"/>
    </svg>
  </section>

  <section class="card card--back">
    <div class="brand-ghost">Ridgeway Sparks</div>
    <h2 class="services-heading">SERVICES I OFFER</h2>
    <ul class="services">
      <li>Breakdowns</li>
      <li>Field Service</li>
      <li>A/C Systems</li>
      <li>Machine rewires</li>
      <li>Mine site vehicle fit outs</li>
    </ul>
  </section>

</div>
</body>
</html>
```